Veltrom Limited Business Card Design Project

Veltrom Limited is my UK based company used as my brand to work as an Interim Manager or contractor in project/programme management and Non-Executive Director.

Veltrom is Latin for 'execute' as in getting things done rather than killing people!

Logo and design needs to promote reliable, professional, and successful project delivery. Simple, elegant, clean, professional are words that should spring to mind!

Target Market(s)

Middle and senior management in english speaking countries aged 35 - 60 that hire and task qualified and experienced project/programme managers and Non-Executive Directors.

Industry/Entity Type

Contractor

Font styles to use
Serif
Sans Serif

Requirements
Must have
• Mobile telephone number 07842 615509
email address peterhollis@veltrom-example.co.uk
Nice to have
• ProfNet link to my profile.

Interim Manager
Should not have
• avoid Ticks and clocks

```html
<!DOCTYPE html>
<html lang="en">
<head>
<meta charset="utf-8">
<title>Veltrom Limited – Business Card</title>
<link href="https://fonts.googleapis.com/css2?family=Exo+2:wght@400;500;600&display=swap" rel="stylesheet">
<style>
  :root{
    --page:#ffffff;
    --card:#353839;
    --accent:#2bb5d0;
    --text:#ffffff;
    --trim:#b5b5b5;
  }
  html,body{margin:0;padding:0;width:1200px;height:1000px;overflow:hidden;background:var(--page);}
  .sheet{position:relative;width:1200px;height:1000px;font-family:"Exo 2",sans-serif;}
  .card{position:absolute;top:420px;width:270px;height:162px;background:var(--card);}
  .card--front{left:310px;}
  .card--back{left:622px;}
  .crop-marks{position:absolute;left:0;top:0;width:1200px;height:1000px;pointer-events:none;}
  .brand{position:absolute;display:flex;align-items:center;gap:10px;color:var(--text);font-weight:500;letter-spacing:1.5px;}
  .brand__square{width:12px;height:12px;background:var(--accent);}
  .card--front .brand{left:60px;top:71px;font-size:17px;}
  .card--back .brand{left:172px;top:71px;font-size:13px;gap:6px;letter-spacing:1px;}
  .card--back .brand__square{width:9px;height:9px;}
  .holder{position:absolute;left:47px;top:32px;}
  .holder__name{color:var(--text);font-size:11px;font-weight:500;line-height:12px;}
  .holder__role{color:var(--accent);font-size:7px;font-weight:600;line-height:9px;}
  .contacts{position:absolute;left:33px;top:91px;margin:0;padding:0;list-style:none;}
  .contacts__item{display:flex;align-items:center;gap:5px;height:13.5px;color:var(--text);font-size:8.5px;}
  .contacts__icon{width:9px;height:9px;flex:none;}
</style>
</head>
<body>
<div class="sheet">
  <svg class="crop-marks" viewBox="0 0 1200 1000" aria-hidden="true">
    <g stroke="var(--trim)" stroke-width="0.6">
      <line x1="319" y1="411" x2="319" y2="419"/><line x1="570" y1="411" x2="570" y2="419"/>
      <line x1="319" y1="583" x2="319" y2="591"/><line x1="570" y1="583" x2="570" y2="591"/>
      <line x1="301" y1="428" x2="309" y2="428"/><line x1="581" y1="428" x2="589" y2="428"/>
      <line x1="301" y1="573" x2="309" y2="573"/><line x1="581" y1="573" x2="589" y2="573"/>
      <line x1="630" y1="411" x2="630" y2="419"/><line x1="882" y1="411" x2="882" y2="419"/>
      <line x1="630" y1="583" x2="630" y2="591"/><line x1="882" y1="583" x2="882" y2="591"/>
      <line x1="613" y1="428" x2="621" y2="428"/><line x1="893" y1="428" x2="901" y2="428"/>
      <line x1="613" y1="573" x2="621" y2="573"/><line x1="893" y1="573" x2="901" y2="573"/>
    </g>
  </svg>

  <section class="card card--front">
    <div class="brand"><span class="brand__square"></span><span class="brand__name">VELTROM</span></div>
  </section>

  <section class="card card--back">
    <div class="holder">
      <div class="holder__name">Peter Hollis</div>
      <div class="holder__role">Interim Manager</div>
    </div>
    <ul class="contacts">
      <li class="contacts__item">
        <svg class="contacts__icon" viewBox="0 0 10 10"><circle cx="5" cy="5" r="5" fill="var(--accent)"/><path d="M3.3 2.6l1 1-.5.6c.3.7.9 1.3 1.6 1.6l.6-.5 1 1-.7.9C4.8 7 3 5.2 2.6 3.3z" fill="var(--card)"/></svg>
        <span>07842 615509</span>
      </li>
      <li class="contacts__item">
        <svg class="contacts__icon" viewBox="0 0 10 10"><rect x="0.5" y="1.5" width="9" height="7" rx="1" fill="var(--accent)"/><path d="M1 2.2l4 3 4-3" stroke="var(--card)" stroke-width="0.8" fill="none"/></svg>
        <span>peterhollis@veltrom-example.co.uk</span>
      </li>
      <li class="contacts__item">
        <svg class="contacts__icon" viewBox="0 0 10 10"><circle cx="5" cy="5" r="5" fill="var(--accent)"/><path d="M1 5h8M5 1c-1.6 2.4-1.6 5.6 0 8M5 1c1.6 2.4 1.6 5.6 0 8" stroke="var(--card)" stroke-width="0.7" fill="none"/></svg>
        <span>www.veltrom-example.co.uk</span>
      </li>
    </ul>
    <div class="brand"><span class="brand__square"></span><span class="brand__name">VELTROM</span></div>
  </section>
</div>
</body>
</html>
```